Brindle Advisory Business Card Design

Business card for business consulting company, using attached logo. We do financial and strategic consulting, and want a clean, professional image with a bit of fun. Our logo is a flat whale tail, which symbolizes the Orca whale, a highly collaborative, group based animal that is very successful in navigating the ocean, protecting the herd, and hunting. We like the logo that is blue and gray on white one one side, but would be open to a blue card with white lettering on the other side... or whatever you'd suggest
Updates
Hi all - I have had the logo modified to take the shadowing off the tail. I will post it on the brief... under a file name called updated logo. thank you Added Saturday, April 25, 2015
Target Market(s)
Small to medium sized businesses ($10M to $500M in revenue per year), financial and sales executives, general managers, attorneys and CPAs
Industry/Entity Type
Financial
Contact Information for Business Card
Want company name, contact info - name, title, telephone, email, website, linkedin, twitter and Facebook. No physical address yet.
Requirements
Must have
- contemporary design, bold, strong, confident but with a bit of fun. prominently feature the logo and the whale tail icon
Nice to have
- unique touches that would differentiate us from a regular card... for example, logo and writing all on front on white background, but on back - logo in white on a blue background
- open to idea of different shapes of card than standard... but not sure
Should not have
- ?

```html
<!DOCTYPE html>
<html lang="en">
<head>
<meta charset="utf-8">
<title>Brindle Advisory – Business Card</title>
<link href="https://fonts.googleapis.com/css2?family=Open+Sans:wght@400;600;700&display=swap" rel="stylesheet">
<style>
  :root {
    --brand-blue: #0d3a73;
    --brand-gray: #9a9ca0;
    --rule-gray: #b9bbbe;
    --text-gray: #4a4c50;
    --card-white: #ffffff;
    --page-bg: #e9eaec;
  }
  * { margin: 0; padding: 0; box-sizing: border-box; }
  html, body {
    width: 1200px; height: 900px; overflow: hidden;
    background: var(--page-bg);
    font-family: "Open Sans", Arial, sans-serif;
  }
  .canvas { position: relative; width: 1200px; height: 900px; }
  .card {
    position: absolute; left: 100px; top: 164px;
    width: 1000px; height: 572px;
    background: var(--card-white);
    border-radius: 56px;
    overflow: hidden;
    box-shadow: 0 6px 24px rgba(0,0,0,0.12);
  }
  .card-bands { position: absolute; inset: 0; }
  .brand {
    position: absolute; left: 0; right: 0; top: 78px;
    display: flex; flex-direction: column; align-items: center;
  }
  .brand-square {
    width: 92px; height: 92px; border-radius: 14px;
    background: var(--brand-blue);
  }
  .brand-name {
    margin-top: 18px;
    font-size: 66px; font-weight: 600; line-height: 1;
    color: var(--brand-blue); letter-spacing: -1.5px;
  }
  .brand-tagline {
    align-self: flex-end;
    margin-right: 222px; margin-top: 4px;
    font-size: 18px; color: var(--brand-blue);
  }
  .contact {
    position: absolute; left: 0; right: 0; top: 338px;
    display: flex; justify-content: center;
    font-variant: small-caps; letter-spacing: 2.5px;
    color: var(--text-gray); font-size: 21px;
  }
  .contact-person {
    width: 300px; text-align: right; padding-right: 22px;
    line-height: 1.3;
  }
  .person-name { color: var(--brand-blue); font-weight: 700; font-size: 24px; }
  .person-title { margin-bottom: 14px; }
  .contact-divider { width: 2px; background: var(--rule-gray); height: 150px; }
  .contact-lines { width: 340px; padding-left: 18px; list-style: none; }
  .contact-lines li { display: flex; align-items: center; gap: 10px; height: 28px; }
  .contact-lines svg { width: 20px; height: 20px; flex: none; }
</style>
</head>
<body>
<main class="canvas">
  <section class="card" aria-label="Brindle Advisory business card">
    <svg class="card-bands" viewBox="0 0 1000 572" preserveAspectRatio="none" aria-hidden="true">
      <path d="M0 0 H80 Q30 286 80 572 H0 Z" fill="var(--brand-blue)"/>
      <path d="M98 0 Q48 286 98 572" fill="none" stroke="var(--rule-gray)" stroke-width="6"/>
      <path d="M1000 0 H920 Q970 286 920 572 H1000 Z" fill="var(--brand-blue)"/>
      <path d="M902 0 Q952 286 902 572" fill="none" stroke="var(--rule-gray)" stroke-width="6"/>
    </svg>

    <header class="brand">
      <div class="brand-square"></div>
      <div class="brand-name">Brindle Advisory</div>
      <div class="brand-tagline">business consulting</div>
    </header>

    <div class="contact">
      <div class="contact-person">
        <div class="person-name">Daniel Hart</div>
        <div class="person-title">Owner / C.E.O</div>
        <div class="person-address">Suite # 410, Elm Court,<br>NY 10452</div>
      </div>
      <div class="contact-divider"></div>
      <ul class="contact-lines">
        <li><svg viewBox="0 0 20 20"><circle cx="10" cy="10" r="10" fill="var(--text-gray)"/><path d="M6 5 L8 5 L9 8 L8 9 Q9 11 11 12 L12 11 L15 12 L15 14 Q10 15 6 9 Z" fill="#fff"/></svg>555-210-4830</li>
        <li><svg viewBox="0 0 20 20"><circle cx="10" cy="10" r="10" fill="var(--text-gray)"/><rect x="7" y="4" width="6" height="12" rx="1" fill="#fff"/></svg>555-738-1942</li>
        <li><svg viewBox="0 0 20 20"><circle cx="10" cy="10" r="10" fill="var(--text-gray)"/><rect x="5" y="8" width="10" height="7" fill="#fff"/><rect x="7" y="5" width="6" height="3" fill="#fff"/></svg>555-604-2217</li>
        <li><svg viewBox="0 0 20 20"><circle cx="10" cy="10" r="10" fill="var(--text-gray)"/><rect x="5" y="6" width="10" height="8" fill="#fff"/><path d="M5 6 L10 10 L15 6" fill="none" stroke="var(--text-gray)" stroke-width="1.2"/></svg>daniel@brindleadvisory.com</li>
        <li><svg viewBox="0 0 20 20"><circle cx="10" cy="10" r="10" fill="var(--text-gray)"/><circle cx="10" cy="10" r="5.5" fill="none" stroke="#fff" stroke-width="1.3"/><path d="M4.5 10 H15.5 M10 4.5 V15.5" stroke="#fff" stroke-width="1.1"/></svg>www.brindleadvisory.com</li>
      </ul>
    </div>
  </section>
</main>
</body>
</html>
```